Business Broker Graphics Package

Hi,

Seeking a smart and professional graphics package design including business card design (double-sided) and letterhead and PowerPoint slide template.

3 Deliverables:

1. Company Letterhead
2. Business Card (two sided) (will consider one sided designs)
3. PowerPoint Template. Requires cover PPT and 2nd page design.

For the prototype use this info:
Morgan Prelch QTR
Certified Business Intermediary
5817 Larkfield Rd.
Halvern, OR 97321
555.214.3096
Sample@Corvenlane.com
www.CorvenLane.com

I'll give exact information to winner to finalize later.

I've attached the logo..

Business card will be double sided and info for back of card is in attachment.

Look forward to your great ideas and concepts!
Updates

Project Deadline Extended
Reason: Just finalized logo design so now I'm ready to proceed with graphics package. Thanks!

Project Deadline Extended
Reason: More time to complete work! Thanks!

Target Market(s)

President's and business owners, CPA's and other professionals.

Industry/Entity Type

Business

Requirements
Nice to have
• Prefer horizontal card, but will consider vertical card design.

The business card should be all or primarily white. Text colors should be same as logo creative combination of black and forest green.

PowerPoint can be white background or lighter palette of colors I like gold color. I do not like darkly colored PowerPoint designs I prefer light and bright designs.

```html
<!DOCTYPE html>
<html lang="en">
<head>
<meta charset="utf-8">
<title>Corven Lane – Stationery Package</title>
<link rel="stylesheet" href="https://fonts.googleapis.com/css2?family=Tinos:wght@400;700&display=swap">
<style>
  :root{
    --forest:#04612f;
    --forest-dark:#1e3b27;
    --ink:#111111;
    --paper:#ffffff;
    --ghost:#eef0ef;
    --shadow:0 1px 4px rgba(0,0,0,.35);
  }
  html,body{margin:0;padding:0;overflow:hidden;background:var(--paper);}
  .canvas{position:relative;width:1200px;height:1200px;overflow:hidden;background:var(--paper);
    font-family:"Tinos","Times New Roman",serif;color:var(--ink);}
  .sheet{position:absolute;background:var(--paper);box-shadow:var(--shadow);overflow:hidden;}
  .sheet svg.curves{position:absolute;inset:0;width:100%;height:100%;}
  .letterhead{left:74px;top:24px;width:474px;height:614px;}
  .slide{left:18px;top:666px;width:670px;height:500px;}
  .card-front{left:702px;top:610px;width:480px;height:276px;}
  .card-back{left:702px;top:892px;width:480px;height:275px;}

  .brand{position:absolute;line-height:1;display:flex;align-items:center;gap:6px;
    font-family:"Tinos","Times New Roman",serif;font-weight:700;color:var(--forest);white-space:nowrap;}
  .brand-dot{display:inline-block;width:.55em;height:.55em;background:var(--forest);}

  .letterhead .brand{left:22px;top:44px;font-size:19px;}
  .slide .brand{left:22px;top:38px;font-size:19px;}
  .slide .backdrop-name{position:absolute;left:0;right:0;top:236px;text-align:center;line-height:1;
    font-family:"Tinos","Times New Roman",serif;font-weight:700;font-size:68px;color:var(--ghost);white-space:nowrap;}

  .card-front .brand{left:52px;top:118px;font-size:19px;}
  .contact{position:absolute;left:260px;top:70px;width:180px;text-align:center;font-weight:700;font-size:10.5px;line-height:17.3px;font-style:normal;}

  .card-back .brand{left:0;right:0;top:130px;justify-content:center;font-size:42px;gap:12px;}
  .services{position:absolute;left:0;right:0;top:233px;text-align:center;color:var(--ink);}
  .services h2{margin:0;font-family:"Tinos","Times New Roman",serif;font-weight:400;font-size:11.5px;letter-spacing:.3px;text-transform:uppercase;}
  .services ul{list-style:none;margin:2px 0 0;padding:0;display:flex;justify-content:center;gap:7px;font-weight:700;font-size:11.5px;}
  .services li::before{content:"\2713";margin-right:1px;}
</style>
</head>
<body>
<div class="canvas">

  <section class="sheet letterhead" aria-label="Letterhead">
    <svg class="curves" viewBox="0 0 474 614" preserveAspectRatio="none" aria-hidden="true">
      <path d="M244 0 Q420 18 474 66 L474 0 Z" fill="var(--forest)"/>
      <path d="M0 462 Q200 652 474 528 L474 614 L0 614 Z" fill="var(--forest-dark)"/>
      <path d="M0 471 Q200 660 474 537 L474 614 L0 614 Z" fill="var(--forest)"/>
    </svg>
    <div class="brand"><span class="brand-dot"></span>Corven Lane</div>
  </section>

  <section class="sheet slide" aria-label="Presentation slide">
    <svg class="curves" viewBox="0 0 670 500" preserveAspectRatio="none" aria-hidden="true">
      <path d="M342 0 Q590 22 670 92 L670 0 Z" fill="var(--forest)"/>
      <path d="M0 290 Q290 512 670 395 L670 500 L0 500 Z" fill="var(--forest-dark)"/>
      <path d="M0 300 Q290 520 670 405 L670 500 L0 500 Z" fill="var(--forest)"/>
    </svg>
    <div class="backdrop-name" aria-hidden="true">Corven Lane</div>
    <div class="brand"><span class="brand-dot"></span>Corven Lane</div>
  </section>

  <section class="sheet card-front" aria-label="Business card, front">
    <svg class="curves" viewBox="0 0 480 276" preserveAspectRatio="none" aria-hidden="true">
      <path d="M0 180 Q240 240 480 198 L480 276 L0 276 Z" fill="var(--forest-dark)"/>
      <path d="M0 188 Q240 247 480 206 L480 276 L0 276 Z" fill="var(--forest)"/>
    </svg>
    <div class="brand"><span class="brand-dot"></span>Corven Lane</div>
    <address class="contact">
      Morgan Prelch QTR<br>
      Certified Business Intermediary<br>
      5817 Larkfield Rd.<br>
      Halvern, OR 97321<br>
      555.214.3096<br>
      Sample@Corvenlane.com<br>
      Web: www.CorvenLane.com
    </address>
  </section>

  <section class="sheet card-back" aria-label="Business card, back">
    <svg class="curves" viewBox="0 0 480 275" preserveAspectRatio="none" aria-hidden="true">
      <path d="M0 186 Q240 226 480 180 L480 275 L0 275 Z" fill="var(--forest-dark)"/>
      <path d="M0 194 Q240 233 480 188 L480 275 L0 275 Z" fill="var(--forest)"/>
    </svg>
    <div class="brand"><span class="brand-dot"></span>Corven Lane</div>
    <div class="services">
      <h2>Ownership Solutions</h2>
      <ul>
        <li>Sale / Acquisition</li>
        <li>Growth Engineer</li>
        <li>Exit Planning</li>
        <li>Valuation</li>
      </ul>
    </div>
  </section>

</div>
</body>
</html>
```